we need a business card design that shows the customer what we can do for them, in pictures and words. we do tipper work of supplying recycled aggregates, soil removal from site, landscaping, demolition & groundwork and much more.(you can find photo`s and a description on our web site - brackleyplant.co.uk)

brackley plant works ltd, family business doing all aspect`s of machine & tipper lorry work.

```html
<!DOCTYPE html>
<html lang="en">
<head>
<meta charset="utf-8">
<title>Brackley Plant Works – Business Card</title>
<link rel="stylesheet" href="https://fonts.googleapis.com/css2?family=Open+Sans:ital,wght@0,400;0,600;0,700;0,800;1,600;1,700&display=swap">
<style>
  :root {
    --brand-blue: #2f4fa6;
    --brand-red: #e5352b;
    --ink: #1f1f1f;
    --card: #ffffff;
    --stage: #e9e6e1;
  }
  * { box-sizing: border-box; margin: 0; padding: 0; }
  html, body {
    width: 1200px; height: 1023px; overflow: hidden;
    background: var(--stage);
    font-family: "Open Sans", Arial, sans-serif;
  }
  .card {
    position: absolute; left: 150px; top: 252px;
    width: 900px; height: 520px;
    background: var(--card);
    box-shadow: 0 12px 30px rgba(0,0,0,.18);
    overflow: hidden;
  }
  .brand { position: absolute; left: 46px; top: 40px; display: flex; align-items: center; gap: 16px; }
  .brand-square { width: 26px; height: 26px; background: var(--brand-red); }
  .brand-name {
    color: var(--brand-blue); font-weight: 800; font-size: 40px;
    letter-spacing: .5px; line-height: 1;
  }
  .tagline {
    position: absolute; left: 46px; top: 108px; width: 420px;
    color: var(--brand-red); font-style: italic; font-weight: 700;
    font-size: 21px; line-height: 1.25;
  }
  .services { position: absolute; left: 52px; top: 222px; list-style: none; }
  .services li {
    display: flex; align-items: center; gap: 20px;
    font-size: 19px; color: var(--ink); height: 38px;
  }
  .services li::before {
    content: ""; width: 13px; height: 13px; background: var(--brand-red); flex: none;
  }
  .person { position: absolute; right: 64px; top: 118px; text-align: center; }
  .person-name { color: var(--brand-red); font-size: 30px; font-weight: 600; line-height: 1.1; }
  .person-role { color: var(--ink); font-size: 17px; margin-top: 4px; }
  .contacts { position: absolute; right: 56px; top: 228px; text-align: right; }
  .contacts p { font-size: 18px; color: var(--ink); line-height: 31px; }
  .contacts .label { color: var(--brand-red); font-weight: 700; }
  .address-band {
    position: absolute; left: 0; right: 0; bottom: 0; height: 52px;
    background: var(--brand-blue); color: #fff;
    display: flex; align-items: center; justify-content: center;
    font-size: 19px; font-weight: 600; letter-spacing: .3px;
  }
</style>
</head>
<body>
  <article class="card">
    <header class="brand">
      <span class="brand-square"></span>
      <span class="brand-name">BRACKLEY PLANT WORKS</span>
    </header>
    <p class="tagline">Brackley Plant Works Ltd, family business doing all aspects of machine and tipper lorry work</p>
    <ul class="services">
      <li>Demolition</li>
      <li>Groundworks</li>
      <li>Haulage</li>
      <li>Supplying recycled materials</li>
      <li>Landscaping</li>
    </ul>
    <div class="person">
      <p class="person-name">Daniel Hartwell</p>
      <p class="person-role">Demolition and Groundworks</p>
    </div>
    <div class="contacts">
      <p><span class="label">Phone :</span> 07700 900412</p>
      <p><span class="label">Office/Fax:</span> 01632 960518</p>
      <p><span class="label">Email:</span> brackleyplant@mailbox.net</p>
      <p><span class="label">Website:</span> www.brackleyplant.co.uk</p>
    </div>
    <footer class="address-band">Brackley Plant Works 12, Fenwick Lane, Ashcombe SURREY GU9 4XT</footer>
  </article>
</body>
</html>
```